KVR PROTECTIVE COATINGS BROCHURE

To design a 4 page A4 brochure of protective coating system for steel and concrete infrastructure with industrial , telecoms and oil & gas markets.

brochure title; Inorganic siloxane protective coatings for steel and concrete infrastructure
sub title - Non-isocyanate (NISO) Coatings
Products:
- KVR 300 1K solvent free inorganic tintable finish coat for ultra UV durability
- KVR 300 DM 1K solvent free clear coat for protection of steel and concrete substrates, anti graffiti, highly UV resistant
- KVR BASEGUARD 2K epoxy hybrid anti corrosion coating for steel
- KVR TILEMAX 1K glass flake single pack high abrasion resistant coating
- KVR DURAMETAL 1K single component siloxane zinc anti-corrosion coating
- KVR TANO 1K single component intermediate anti-corrosion coating
- KVR 470 2K two component epoxy-siloxane hybrid durable tintable top coat
- KVR DECKSHIELD 2K two component, chemical resistant, durable floor coating.
- KVR STONEWEAR 2K two component ceramically filled epoxy for high abrasion resistance.

use good clear images of markets sectors (oil&gas, Telecoms, Industrial)
use icons for low VOC, low toxicity, Green, high weathering resistance, chemical resistance, maintenance friendly, environment friendly, non-isocyanate.

Table of primers and top coats in attachment, please use images within document about tinting products

Company Info
Tel +44 (0) 1632 960518
Email sales@tq-hr.example
Address 7-8 Larkwell Meadow Trade Park, Fennick Lane, United Kingdom
web www.tq-hr.example

Target Market(s)

Protective Coatings

Requirements
Must have
• Clear images of target markets and good layout of information provided

```html
<!DOCTYPE html>
<html lang="en">
<head>
<meta charset="utf-8">
<title>KVR Protective Coatings Brochure</title>
<link href="https://fonts.googleapis.com/css2?family=Poppins:wght@400;500;600;700&display=swap" rel="stylesheet">
<style>
:root{
  --navy:#1f4c98;
  --navy-deep:#173d80;
  --sky:#5aaee0;
  --cyan:#2bc4f2;
  --row:#d4e9f8;
  --row-alt:#e6e6e6;
  --white:#ffffff;
  --ink:#1d2b44;
  --stage:#c9c9c9;
}
*{box-sizing:border-box;margin:0;padding:0}
html,body{width:825px;height:1200px;overflow:hidden}
body{background:var(--stage);font-family:'Poppins',sans-serif;color:var(--ink);position:relative}
.page{position:absolute;width:327px;height:463px;overflow:hidden;background:var(--white);box-shadow:0 6px 14px rgba(0,0,0,.25)}
.page--cover{left:66px;top:112px}
.page--back{left:432px;top:112px}
.page--products{left:66px;top:625px}
.page--tint{left:432px;top:625px}
.abs{position:absolute}
.center{left:0;right:0;text-align:center}

/* cover */
.cover-backdrop{left:0;top:0;width:327px;height:300px;background:linear-gradient(180deg,#fff 0%,#eef0f3 45%,#dfe3e8 100%)}
.brand{display:flex;align-items:center;gap:6px;justify-content:center}
.brand-dot{width:14px;height:14px;border-radius:50%;background:var(--navy)}
.brand-name{font-weight:700;font-size:15px;color:var(--navy)}
.cover-brand{left:40px;top:35px;width:247px;height:50px;background:var(--white)}
.cover-art{left:0;top:0}
.cover-kicker{top:329px;font-size:10.5px;font-weight:500;color:var(--white)}
.cover-title{top:345px;font-size:19px;line-height:21px;font-weight:700;color:var(--white)}
.cover-rule{left:42px;top:393px;width:243px;height:1px;background:var(--sky)}
.cover-rule-accent{left:145px;top:392px;width:37px;height:2px;background:var(--sky)}
.cover-sub{top:401px;font-size:11.5px;color:var(--white)}
.cover-web{top:433px;font-size:8.5px;letter-spacing:3px;color:var(--white)}
.cover-web b{color:var(--sky);font-weight:500}

/* back */
.back-photo{left:0;top:0;width:327px;height:300px;background:linear-gradient(180deg,#c9ccd1 0%,#9aa3ae 40%,#6f8bb0 75%,#4b6ea6 100%)}
.back-brand{top:270px}
.back-brand .brand-name{color:var(--white);font-size:13px}
.back-brand .brand-dot{background:var(--white)}
.back-heading{top:320px;font-size:8.5px;font-weight:600;letter-spacing:1.2px;color:var(--sky)}
.contact-icon{width:13px;height:13px;left:157px;border-radius:50%;background:var(--white)}
.contact-text{font-size:8.5px;color:var(--white);line-height:10px}

/* products page */
.products-panel{left:0;top:0;width:327px;height:186px;background:linear-gradient(135deg,#2a5aa8,#1c4790);border-radius:0 0 40px 40px}
.products-heading{left:18px;top:15px;font-size:14px;font-weight:700;color:var(--white)}
.products-heading span{color:var(--cyan)}
.product{width:135px}
.product-name{font-size:6.2px;font-weight:700;color:var(--cyan);line-height:8px}
.product-name::before{content:"";display:inline-block;width:3px;height:3px;border-radius:50%;background:var(--cyan);margin-right:3px;vertical-align:middle}
.product-desc{font-size:4.8px;line-height:5.8px;color:var(--white)}
.table-title{height:16px;border-radius:8px;background:var(--navy);color:var(--white);font-size:9.5px;font-weight:700;text-align:center;line-height:16px}
.spec-table{display:grid;gap:1.5px}
.spec-head{background:var(--sky);color:var(--white);font-size:5px;font-weight:600;text-align:center;line-height:9px;height:9px;border-radius:3px 3px 0 0}
.spec-cell{background:var(--row-alt);font-size:4.6px;text-align:center;display:flex;align-items:center;justify-content:center;line-height:5.5px;padding:0 2px}
.spec-cell.name{background:var(--row);justify-content:flex-start;font-weight:600}
.spec-cell.dft{background:var(--row)}
.footer-web{left:19px;top:433px;width:74px;height:11px;background:var(--navy);color:var(--white);font-size:6px;line-height:11px;padding-left:6px;clip-path:polygon(0 0,92% 0,100% 100%,0 100%)}
.footer-line{left:90px;top:443px;width:196px;height:1px;background:var(--navy)}
.footer-num{left:286px;top:435px;width:12px;height:12px;border-radius:50%;background:var(--navy);border:1.5px solid var(--sky);color:var(--white);font-size:6.5px;font-weight:600;text-align:center;line-height:9px}

/* tint page */
.tint-photo{left:0;top:0;width:327px;height:79px;background:linear-gradient(135deg,#2f5da3,#1d478c 60%,#2b5aa2)}
.tint-image{border-radius:5px;overflow:hidden;background:#dcecf8}
.tint-image .fill{position:absolute;left:2px;top:2px;right:2px}
.tint-image .label{position:absolute;left:0;right:0;bottom:1px;text-align:center;font-size:7px;font-weight:500;color:var(--navy)}
.tech-panel{left:163px;top:167px;width:145px;height:256px;border-radius:7px;background:linear-gradient(160deg,#24529e,#1b4588)}
.tech-heading{left:8px;top:8px;font-size:9.5px;line-height:10px;font-weight:700;color:var(--white);border-bottom:1px solid var(--white);padding-bottom:2px}
.tech-item{left:9px;display:flex;align-items:center;gap:5px;color:var(--white);font-size:7.5px;font-weight:500;line-height:8px}
.tech-icon{width:16px;height:16px;border-radius:50%;border:1px solid var(--white);background:#2f63b3;flex:none}
</style>
</head>
<body>

<!-- Cover -->
<section class="page page--cover">
  <div class="abs cover-backdrop" role="img" aria-label="Faded industrial plant in the background"></div>
  <div class="abs cover-brand brand"><span class="brand-dot"></span><span class="brand-name">Kestrel Vane Resins</span></div>
  <svg class="abs cover-art" width="327" height="463" viewBox="0 0 327 463">
    <path d="M0 318 Q40 250 80 238 L250 238 Q300 255 327 318 L327 463 L0 463 Z" fill="var(--sky)"/>
    <path d="M0 333 Q50 262 95 252 L235 252 Q290 265 327 333 L327 463 L0 463 Z" fill="var(--navy)"/>
    <circle cx="164" cy="212" r="106" fill="var(--navy)"/>
    <path d="M58 245 A106 106 0 0 0 270 245 Z" fill="var(--sky)"/>
    <circle cx="163" cy="206" r="97" fill="var(--white)"/>
  </svg>
  <div class="abs" style="left:70px;top:113px;width:186px;height:186px;border-radius:50%;background:radial-gradient(circle at 55% 45%,#e2782f,#b84a1c 45%,#3c4b60 80%)" role="img" aria-label="Worker spray painting orange steel beams"></div>
  <p class="abs center cover-kicker">INORGANIC SILOXANE PROTECTIVE COATINGS FOR</p>
  <h1 class="abs center cover-title">STEEL, GALVANIZED AND<br>CONCRETE INFRASTRUCTURE</h1>
  <div class="abs cover-rule"></div><div class="abs cover-rule-accent"></div>
  <p class="abs center cover-sub">Non-isocyanate (NISO) Coatings</p>
  <p class="abs center cover-web">WWW.<b>TQ-HR</b>.EXAMPLE</p>
</section>

<!-- Back cover -->
<section class="page page--back">
  <div class="abs back-photo" role="img" aria-label="Glossy coated floor in an underground car park"></div>
  <svg class="abs" style="left:0;top:0" width="327" height="463" viewBox="0 0 327 463">
    <path d="M0 312 Q164 170 327 312 L327 463 L0 463 Z" fill="var(--sky)"/>
    <path d="M0 320 Q164 180 327 320 L327 463 L0 463 Z" fill="var(--white)"/>
    <path d="M0 324 Q164 186 327 324 L327 463 L0 463 Z" fill="var(--navy)"/>
  </svg>
  <div class="abs center brand back-brand"><span class="brand-dot"></span><span class="brand-name">Kestrel Vane Resins</span></div>
  <p class="abs center back-heading">KESTREL VANE RESINS INORGANIC INNOVATION</p>
  <svg class="abs contact-icon" style="top:340px" viewBox="0 0 13 13"><path d="M4 3.5 L5.3 5 L4.7 5.8 Q5.6 7.5 7.2 8.3 L8 7.7 L9.5 9 L8.7 10 Q5 9.5 3 5 Z" fill="var(--navy)"/></svg>
  <p class="abs center contact-text" style="top:358px">+44 (0) 1632 960518</p>
  <svg class="abs contact-icon" style="top:376px" viewBox="0 0 13 13"><rect x="3" y="4" width="7" height="5" fill="var(--navy)"/><path d="M3 4 L6.5 7 L10 4" stroke="var(--white)" stroke-width=".7" fill="none"/></svg>
  <p class="abs center contact-text" style="top:392px">sales@tq-hr.example</p>
  <svg class="abs contact-icon" style="top:410px" viewBox="0 0 13 13"><path d="M6.5 10.5 L4 6.5 A2.8 2.8 0 1 1 9 6.5 Z" fill="var(--navy)"/><circle cx="6.5" cy="5.3" r="1" fill="var(--white)"/></svg>
  <p class="abs center contact-text" style="top:427px">7-8 Larkwell Meadow Trade Park,<br>Fennick Lane, United Kingdom</p>
</section>

<!-- Products page -->
<section class="page page--products">
  <div class="abs products-panel" role="img" aria-label="Blue tinted photo of coating application"></div>
  <h2 class="abs products-heading">OUR <span>PRODUCTS</span></h2>

  <div class="abs product" style="left:19px;top:38px"><p class="product-name">KVR 300 1K</p><p class="product-desc">Solvent free inorganic tintable finish coat for ultra UV durability</p></div>
  <div class="abs product" style="left:19px;top:64px"><p class="product-name">KVR 300 DM 1K</p><p class="product-desc">Solvent free clear coat for protection of steel and concrete substrates, anti graffiti, highly UV resistant</p></div>
  <div class="abs product" style="left:19px;top:97px"><p class="product-name">KVR TANO 1K</p><p class="product-desc">Single component intermediate anti-corrosion coating</p></div>
  <div class="abs product" style="left:19px;top:124px"><p class="product-name">KVR TILEMAX 1K</p><p class="product-desc">Glass flake single pack high abrasion resistant coating</p></div>
  <div class="abs product" style="left:19px;top:151px"><p class="product-name">KVR DURAMETAL 1K</p><p class="product-desc">Single component siloxane zinc anti-corrosion coating</p></div>

  <div class="abs product" style="left:170px;top:38px"><p class="product-name">KVR BASEGUARD 2K</p><p class="product-desc">Epoxy hybrid anti corrosion coating for steel</p></div>
  <div class="abs product" style="left:170px;top:61px"><p class="product-name">KVR 470 2K</p><p class="product-desc">Two component epoxy-siloxane hybrid durable tintable top coat</p></div>
  <div class="abs product" style="left:170px;top:90px"><p class="product-name">KVR DECKSHIELD 2K</p><p class="product-desc">Two component, chemical resistant, durable floor coating.</p></div>
  <div class="abs product" style="left:170px;top:119px"><p class="product-name">KVR STONEWEAR 2K</p><p class="product-desc">Two component ceramic filled epoxy for high abrasion resistance.</p></div>

  <div class="abs table-title" style="left:18px;top:197px;width:292px">1 AND 2 COMPONENT SILOXANE BASED COATINGS</div>
  <div class="abs spec-table" style="left:18px;top:219px;width:292px;grid-template-columns:52px 48px 80px 51px 52px;grid-template-rows:9px repeat(9,18.5px)">
    <div class="spec-head">PRODUCT</div><div class="spec-head">COMPONENTS</div><div class="spec-head">FUNCTIONALITY</div><div class="spec-head">CHEMISTRY</div><div class="spec-head">DFT (µM)</div>
    <div class="spec-cell name">KVR TANO 1K</div><div class="spec-cell">1</div><div class="spec-cell">Anti-corrosion Primer</div><div class="spec-cell">Siloxane</div><div class="spec-cell dft">150 - 200</div>
    <div class="spec-cell name">KVR DURAMETAL 1K</div><div class="spec-cell">1</div><div class="spec-cell">Anti-corrosion Primer</div><div class="spec-cell">Siloxane-Zinc</div><div class="spec-cell dft">75-100</div>
    <div class="spec-cell name">KVR TILEMAX 1K</div><div class="spec-cell">1</div><div class="spec-cell">Abrasion resistant Primer</div><div class="spec-cell">Siloxane-Ceramic</div><div class="spec-cell dft">200-250</div>
    <div class="spec-cell name">KVR 300 1K</div><div class="spec-cell">1</div><div class="spec-cell">Durable Topcoat</div><div class="spec-cell">Siloxane</div><div class="spec-cell dft">75-150</div>
    <div class="spec-cell name">KVR 300 DM 1K</div><div class="spec-cell">1</div><div class="spec-cell">Durable clear coat<br>(anti-graffiti)</div><div class="spec-cell">Siloxane</div><div class="spec-cell dft">25-50</div>
    <div class="spec-cell name">KVR BASEGUARD 2K</div><div class="spec-cell">2</div><div class="spec-cell">Anti-corrosion Primer</div><div class="spec-cell">Epoxy-Hybrid</div><div class="spec-cell dft">100 - 200</div>
    <div class="spec-cell name">KVR STONEWEAR 2K</div><div class="spec-cell">2</div><div class="spec-cell">Abrasion resistant Primer</div><div class="spec-cell">Epoxy-Ceramic</div><div class="spec-cell dft">200-250</div>
    <div class="spec-cell name">KVR 470 2K</div><div class="spec-cell">2</div><div class="spec-cell">Durable Topcoat</div><div class="spec-cell">Siloxane-Hybrid</div><div class="spec-cell dft">75-150</div>
    <div class="spec-cell name">KVR DECKSHIELD 2K</div><div class="spec-cell">2</div><div class="spec-cell">UV durable floor coating</div><div class="spec-cell">Siloxane-Hybrid</div><div class="spec-cell dft">200-250</div>
  </div>

  <div class="abs footer-web">www.tq-hr.example</div>
  <div class="abs footer-line"></div>
  <div class="abs footer-num">1</div>
</section>

<!-- Tinting page -->
<section class="page page--tint">
  <div class="abs tint-photo" role="img" aria-label="Blue tinted photo of a worker spraying a coating"></div>
  <div class="abs table-title" style="left:18px;top:69px;width:291px;background:var(--sky)">TINTABLE TOP COATS</div>
  <div class="abs spec-table" style="left:18px;top:90px;width:291px;grid-template-columns:52px 48px 81px 68px 36px;grid-template-rows:9px repeat(3,19px)">
    <div class="spec-head">PRODUCT</div><div class="spec-head">COMPONENTS</div><div class="spec-head">FUNCTIONALITY</div><div class="spec-head">TINTABLE COLOURS</div><div class="spec-head">DFT (µM)</div>
    <div class="spec-cell name">KVR 300 1K</div><div class="spec-cell">1</div><div class="spec-cell">Durable Topcoat</div><div class="spec-cell">RAL, BS &amp; Custom</div><div class="spec-cell dft">75-150</div>
    <div class="spec-cell name">KVR 470 2K</div><div class="spec-cell">1</div><div class="spec-cell">Durable Topcoat</div><div class="spec-cell">RAL, BS &amp; Custom</div><div class="spec-cell dft">75-150</div>
    <div class="spec-cell name">KVR DECKSHIELD 2K</div><div class="spec-cell">1</div><div class="spec-cell">UV durable floor coating</div><div class="spec-cell">RAL, BS &amp; Custom</div><div class="spec-cell dft">200-250</div>
  </div>

  <div class="abs tint-image" style="left:18px;top:167px;width:126px;height:157px">
    <div class="fill" style="height:141px;background:linear-gradient(180deg,#d9d9d9,#9a9a9a 60%,#c8ccd2)" role="img" aria-label="Tint machine dispensing colourant into a paint tin"></div>
    <p class="label">Tint machine</p>
  </div>
  <div class="abs tint-image" style="left:18px;top:332px;width:126px;height:91px">
    <div class="fill" style="height:75px;background:linear-gradient(180deg,#e9d9a8,#e07a4a 25%,#b8434e 45%,#3e6fb0 62%,#3c8a6a 78%,#8a8a86)" role="img" aria-label="RAL colour chart swatches"></div>
    <p class="label">RAL, BS and Custom Colours</p>
  </div>

  <div class="abs tech-panel">
    <h3 class="abs tech-heading">OUR COATING<br>TECHNOLOGIES INCLUDE</h3>
    <div class="abs tech-item" style="top:37px"><span class="tech-icon"></span>Low VOC</div>
    <div class="abs tech-item" style="top:60px"><span class="tech-icon"></span>Low toxicity</div>
    <div class="abs tech-item" style="top:84px"><span class="tech-icon"></span>Green</div>
    <div class="abs tech-item" style="top:107px"><span class="tech-icon"></span>High weathering<br>resistance</div>
    <div class="abs tech-item" style="top:133px"><span class="tech-icon"></span>Maintenance friendly</div>
    <div class="abs tech-item" style="top:157px"><span class="tech-icon"></span>Environment friendly</div>
    <div class="abs tech-item" style="top:181px"><span class="tech-icon"></span>Non-isocyanate</div>
    <div class="abs tech-item" style="top:206px"><span class="tech-icon"></span>Chemical resistance</div>
    <div class="abs tech-item" style="top:230px"><span class="tech-icon"></span>Low Carbon</div>
  </div>

  <div class="abs footer-web">www.tq-hr.example</div>
  <div class="abs footer-line"></div>
  <div class="abs footer-num">2</div>
</section>

</body>
</html>
```